Varnel Supply requires a new business card.

We are an online professional tool store.

Target Market(s)

We target the professional technician.

Industry/Entity Type

Business

Contact Information for Business Card

VarnelSupply.com.au

sales@varnelsupply.example

Requirements
Must have
• Needs to look commercial and professional
Should not have
• No Australian Colors, maps or shapes.
• No Shapes of Tools

```html
<!DOCTYPE html>
<html lang="en">
<head>
<meta charset="utf-8">
<title>Varnel Supply – Business Card</title>
<link rel="stylesheet" href="https://fonts.googleapis.com/css2?family=Open+Sans:wght@400;600;700&display=swap">
<style>
  :root {
    --page-bg: #ecebe8;
    --card-blue: #0b29b8;
    --accent-cyan: #0b93c8;
    --card-white: #f7f7f7;
    --text-light: #ffffff;
    --brand-blue: #1a34b8;
  }
  html, body {
    margin: 0;
    padding: 0;
    width: 1200px;
    height: 900px;
    overflow: hidden;
    background: var(--page-bg);
    font-family: "Open Sans", Arial, sans-serif;
  }
  .canvas {
    position: relative;
    width: 1200px;
    height: 900px;
  }
  .card {
    position: absolute;
    box-shadow: 0 6px 18px rgba(0,0,0,0.18);
  }
  .card--contact {
    left: 78px;
    top: 34px;
    width: 588px;
    height: 364px;
    background: var(--card-blue);
    color: var(--text-light);
    overflow: hidden;
  }
  .card--brand {
    left: 388px;
    top: 505px;
    width: 566px;
    height: 352px;
    background: var(--card-white);
    display: flex;
    align-items: center;
    justify-content: center;
  }
  .decor-area {
    position: absolute;
    left: 0;
    top: 0;
    width: 300px;
    height: 364px;
    background: linear-gradient(100deg, rgba(11,147,200,0.85) 0%, rgba(11,147,200,0.45) 55%, rgba(11,147,200,0) 100%);
  }
  .identity {
    position: absolute;
    right: 36px;
    top: 44px;
    text-align: right;
  }
  .identity__name {
    margin: 0;
    font-size: 20px;
    font-weight: 400;
    line-height: 26px;
  }
  .identity__role {
    margin: 0;
    font-size: 15px;
    line-height: 18px;
  }
  .contact-list {
    position: absolute;
    right: 36px;
    top: 181px;
    margin: 0;
    padding: 0;
    list-style: none;
    text-align: right;
    font-size: 15px;
    line-height: 21.5px;
  }
  .contact-list li {
    display: flex;
    justify-content: flex-end;
    align-items: center;
    gap: 7px;
  }
  .contact-list svg {
    width: 12px;
    height: 12px;
    fill: var(--text-light);
  }
  .address {
    position: absolute;
    right: 36px;
    top: 281px;
    margin: 0;
    text-align: right;
    font-size: 15px;
    line-height: 21px;
    font-style: normal;
  }
  .brand-mark {
    display: flex;
    align-items: center;
    gap: 14px;
    color: var(--brand-blue);
    font-size: 40px;
    font-weight: 700;
    letter-spacing: 0.5px;
  }
  .brand-mark__dot {
    width: 34px;
    height: 34px;
    border-radius: 50%;
    background: var(--accent-cyan);
  }
</style>
</head>
<body>
<main class="canvas">
  <section class="card card--contact">
    <div class="decor-area" role="img" aria-label="Geometric decoration in light blue"></div>
    <div class="identity">
      <p class="identity__name">Daniel Hartwell</p>
      <p class="identity__role">Managing Director</p>
    </div>
    <ul class="contact-list">
      <li>044-555 210 387
        <svg viewBox="0 0 12 12" aria-hidden="true"><path d="M3.5 0h5a1 1 0 0 1 1 1v10a1 1 0 0 1-1 1h-5a1 1 0 0 1-1-1V1a1 1 0 0 1 1-1zm.5 1.5v8h4v-8zm2 8.6a.6.6 0 1 0 0 1.2.6.6 0 0 0 0-1.2z"/></svg>
      </li>
      <li>044-555 210 387
        <svg viewBox="0 0 12 12" aria-hidden="true"><path d="M1 3.5C1 2 3 1.5 6 1.5s5 .5 5 2v1H8.5v-1h-5v1H1zM3 6l1-1.5h4L9 6v4.5H3zm3 .8a1.4 1.4 0 1 0 0 2.8 1.4 1.4 0 0 0 0-2.8z"/></svg>
      </li>
      <li>sales@varnelsupply.example
        <svg viewBox="0 0 12 12" aria-hidden="true"><path d="M0 2h12v8H0zm1 1v.4l5 3.2 5-3.2V3zm0 1.6V9h10V4.6L6 7.8z"/></svg>
      </li>
      <li>www.VarnelSupply.com.au
        <svg viewBox="0 0 12 12" aria-hidden="true"><circle cx="6" cy="6" r="5.5"/></svg>
      </li>
    </ul>
    <address class="address">48 Kessler Road<br>Northgate, 4013.</address>
  </section>

  <section class="card card--brand">
    <div class="brand-mark">
      <span class="brand-mark__dot" aria-hidden="true"></span>
      <span class="brand-mark__name">Varnel Supply</span>
    </div>
  </section>
</main>
</body>
</html>
```